Newsletter Design Project

We need a newsletter design for our foundation based in the Philippines. We are a child care organization that works for the promotion and protection of children's rights. The newsletter design should be created in PostLoom to be used on our Joomla website. The design should reflect the style and coulours of our website design. It should be compatible to view in web browsers and email applications. You can view our website at: www.brindlecovefoundation.org

If this process goes well, we would be interested to redesign our Carry the Lantern website (www.carrythelantern.net)
Updates

Reason: To give enough time for adjustment to a design a may like. I will have to share them with others whom I work with to get their feedback.

Reason: I'm interested in more designs and giving time for one designer to work with the code for my design template...

Target Market(s)

Youth/Adults/NGOs/Donors, etc

Industry/Entity Type

Foundation

Requirements
Must have
• must have menu
Donate button

```html
<!DOCTYPE html>
<html lang="en">
<head>
<meta charset="utf-8">
<title>Brindle Cove Foundation Newsletter</title>
<link href="https://fonts.googleapis.com/css2?family=Arimo:ital,wght@0,400;0,700;1,400&family=Gelasio:ital,wght@0,400;1,400&family=Caveat:wght@400&display=swap" rel="stylesheet">
<style>
:root{
  --page:#ececec;
  --rust:#a33500;
  --rust-deep:#5a230a;
  --cream:#f7dfa0;
  --quote:#9b3a0a;
  --ink:#2b1a10;
  --gold:#f5c96a;
  --grey-text:#555;
  --ring:#d4d4d4;
  --white:#fff;
}
*{box-sizing:border-box;margin:0;padding:0}
html,body{width:1200px;height:900px;overflow:hidden}
body{background:var(--page);font-family:"Arimo",Arial,sans-serif;position:relative;color:var(--ink)}
.abs{position:absolute}
.preheader{left:300px;top:7px;font-size:7px;color:#777}
.preheader a{color:#777}
.newsletter{left:189px;top:38px;width:415px;height:713px;background:var(--rust);box-shadow:0 14px 14px -6px rgba(0,0,0,.35)}
.masthead{height:75px;background:var(--white);position:relative}
.brand-name{position:absolute;left:0;right:0;top:27px;text-align:center;font-family:"Arimo",Arial,sans-serif;font-size:20px;font-weight:400;color:#222}
.band{height:9px;background:var(--rust-deep)}
.nav{height:46px;position:relative;display:flex;align-items:center;padding:0 10px 8px;font-size:6px;color:var(--white)}
.nav span{margin-right:13px}
.nav i{font-style:normal;margin-right:13px}
.dots{border-top:1px dashed rgba(255,230,200,.7);position:absolute;left:6px;right:6px}
.quote-block{position:relative;height:225px;background:var(--cream)}
.quote-mark{position:absolute;font-family:"Gelasio",Georgia,serif;font-size:38px;color:var(--quote)}
.quote{position:absolute;left:28px;width:350px;top:56px;text-align:center;font-family:"Gelasio",Georgia,serif;font-style:italic;font-size:15px;line-height:18px;color:var(--quote)}
.mission{position:absolute;left:10px;right:14px;top:182px;font-size:7.6px;font-style:italic;line-height:9px;color:var(--ink)}
.donate-btn{position:absolute;display:flex;align-items:center;justify-content:center;background:linear-gradient(#fff,#dcdcdc);border:3px solid #6a2406;border-radius:20px;color:#333;font-weight:400}
.donate-note{position:absolute;text-align:center;font-style:italic;color:var(--white)}
.section-title{position:absolute;font-size:7px;font-weight:700;color:var(--gold)}
.campaign{position:absolute;left:26px;top:572px;width:164px;height:46px;border-bottom:1px solid rgba(255,255,255,.3);font-family:"Gelasio",Georgia,serif;font-size:19px;white-space:nowrap;color:#e9e0d4;display:flex;align-items:center;justify-content:center}
.campaign-note{position:absolute;left:26px;top:628px;width:164px;text-align:center;font-family:"Gelasio",Georgia,serif;font-size:6.5px;color:#f3e6d6}
.vline{position:absolute;left:213px;top:568px;height:82px;border-left:1px dashed rgba(255,230,200,.7)}
.socials{position:absolute;left:261px;top:587px;display:flex;gap:5px}
.socials span{width:25px;height:25px;background:#e6c1ad;border-radius:4px;font-size:5.5px;color:var(--rust-deep);display:flex;align-items:center;justify-content:center}
.copyright{position:absolute;left:0;right:0;bottom:0;height:20px;background:var(--rust-deep);color:var(--white);font-size:7px;display:flex;align-items:center;justify-content:center}
.utility{left:192px;top:799px;font-size:7px;color:#333;display:flex;gap:18px}
.utility a{color:#333;font-weight:700}
.address{left:192px;top:818px;font-size:7px;line-height:10px;color:#444}
.contact{left:192px;top:877px;font-size:7px;color:#444}
.heading{left:730px;top:28px;font-family:"Caveat",cursive;font-weight:400;font-size:42px;color:#666}
.features{font-size:11.5px;line-height:13.2px;color:var(--grey-text)}
.features .sub{padding-left:7px;color:#777}
.zoom-ring{left:634px;top:237px;width:402px;height:400px;border-radius:50%;background:var(--ring)}
.zoom-pointer{left:612px;top:412px}
.zoom-lens{left:659px;top:262px;width:352px;height:352px;border-radius:50%;overflow:hidden;background:var(--rust)}
.lens-cream{position:absolute;left:0;top:0;width:100%;height:106px;background:var(--cream)}
.lens-text{position:absolute;left:24px;top:41px;width:520px;font-size:12px;font-style:italic;line-height:16px;color:var(--ink);white-space:nowrap}
</style>
</head>
<body>

<p class="abs preheader">Having trouble viewing this mail? <a href="#">View it in your browser.</a></p>

<article class="abs newsletter">
  <header class="masthead">
    <div class="brand-name">Brindle Cove Foundation Inc.</div>
  </header>
  <div class="band"></div>
  <nav class="nav">
    <span>HOME</span><i>|</i><span>ABOUT US</span><i>|</i><span>WHAT WE DO</span><i>|</i><span>RESOURCES</span><i>|</i><span>CONTRIBUTE</span><i>|</i><span>PARTNERS</span><i>|</i><span>GALERY</span>
    <div class="dots" style="top:36px"></div>
  </nav>
  <section class="quote-block">
    <div class="quote-mark" style="left:10px;top:18px">“</div>
    <p class="quote">There are millions of children around the world who are victims of sexual abuse, and yet very little is being done to help them and to prevent more from following their path of victimization</p>
    <div class="quote-mark" style="right:12px;top:104px">”</div>
    <p class="mission">Our organization helps victims of sex abuse realize their abilities, hopes and dreams in a society which will protect their rights as human beings and will hold equality, justice, spirituality, health, education, family, community, and the environment as the guiding values and principles for their holistic development.</p>
  </section>
  <div class="dots" style="top:366px"></div>
  <a class="donate-btn" style="left:144px;top:401px;width:126px;height:36px;font-size:12px">DONATE NOW</a>
  <p class="donate-note" style="left:110px;top:453px;width:195px;font-size:7px;line-height:9px">With Your Donation, You Help Us<br>Fight Sexual Abuse on Childs<br>:)</p>
  <div class="dots" style="top:510px"></div>
  <div class="section-title" style="left:33px;top:543px">BRAKE THE SILENCE</div>
  <div class="section-title" style="left:309px;top:543px">SPREAD THE VOICE</div>
  <div class="campaign">Carry the Lantern</div>
  <p class="campaign-note">Stop child sexual abuse and explotation</p>
  <div class="vline"></div>
  <div class="socials"><span>Chatter</span><span>Pipit</span><span>Reelbox</span><span>Snapdot</span></div>
  <footer class="copyright">Copyright © 2012 Brindle Cove Foundation Inc. All Right Reserved</footer>
</article>

<div class="abs utility"><a href="#">send to a friend</a><span>|</span><a href="#">Unsubscribe from this list</a><span>|</span><a href="#">Update preferences</a></div>
<p class="abs address">Brgy. Malaya<br>San Teodoro<br>Oriental Mindoro<br>5210<br>Philippines</p>
<a class="abs contact" href="#">Contact Us</a>

<h2 class="abs heading">Template includes:</h2>
<div class="abs features" style="left:668px;top:92px">
  <div>- Test in all mjaor email clients such as:</div>
  <div class="sub">*Deskmail 03/07/10</div>
  <div class="sub">*Orchard Mail</div>
  <div class="sub">*Gleam Mail</div>
  <div class="sub">*Ember Mail</div>
  <div class="sub">*Yodel Mail</div>
  <div class="sub">*Atlas Mail</div>
  <div class="sub">*Stormwing</div>
  <div class="sub">*Lattice Notes</div>
  <div class="sub">*And More...</div>
</div>
<div class="abs features" style="left:895px;top:92px">
  <div>- Test in SPAM filters</div>
  <div>- Integration to <i>PostLoom</i></div>
  <div>-&nbsp; Maximun Compatibility with major devices</div>
  <div>- <u>Unlimited Revisions</u></div>
</div>

<svg class="abs zoom-pointer" width="30" height="50" viewBox="0 0 30 50"><polygon points="30,0 2,25 30,50" fill="#d4d4d4"/></svg>
<div class="abs zoom-ring"></div>
<div class="abs zoom-lens">
  <div class="lens-cream"></div>
  <p class="lens-text">s of sex abuse realize their abilities, hopes and dreams in a society<br>n beings and will hold equality, justice, spirituality, health, education<br>ronment as the guiding values and principles for their holistic development.</p>
  <div class="dots" style="top:120px;left:10px;right:10px"></div>
  <a class="donate-btn" style="left:83px;top:170px;width:184px;height:52px;font-size:17px;border-width:4px;border-radius:28px">DONATE NOW</a>
  <p class="donate-note" style="left:60px;top:246px;width:232px;font-size:11px;line-height:13px">With Your Donation, You Help Us<br>Fight Sexual Abuse on Childs<br>:)</p>
  <div class="dots" style="top:330px;left:10px;right:10px"></div>
</div>

</body>
</html>
```